Banner Ad Design Project

I place ads in Clickrow and also get traffic from sites like http://www.wellspringlistings.example.au/ to offer our free meditation CD and report at http://quietmindful.example.au/get-the-free-meditation-cd
We need new designs to improve this campaign.
Target Market(s)
40+ year old women, looking for personal growth or help with stress, depression, anxiety, sleep problems, health issues, memory/concentration issues
Industry/Entity Type
Campaign

```html
<!DOCTYPE html>
<html lang="en">
<head>
<meta charset="utf-8">
<title>Free Meditation CD Banner</title>
<link href="https://fonts.googleapis.com/css2?family=Open+Sans:wght@600;700&display=swap" rel="stylesheet">
<style>
  :root {
    --page: #ffffff;
    --band-dark: #050505;
    --band-mid: #1c1c1c;
    --ink: #ffffff;
    --disc-light: #c9dcef;
    --disc-mid: #6f9cc9;
    --disc-deep: #2e5f93;
  }
  * { margin: 0; padding: 0; box-sizing: border-box; }
  html, body {
    width: 1200px;
    height: 168px;
    overflow: hidden;
    background: var(--page);
  }
  .banner {
    position: relative;
    width: 1200px;
    height: 168px;
    font-family: "Open Sans", Arial, sans-serif;
    color: var(--ink);
  }
  .band {
    position: absolute;
    left: 18px;
    top: 22px;
    width: 1164px;
    height: 123px;
    background: radial-gradient(ellipse at 50% 50%, var(--band-mid) 0%, var(--band-dark) 75%);
  }
  .headline {
    position: absolute;
    left: 30px;
    top: 27px;
    font-size: 37px;
    font-weight: 600;
    line-height: 44px;
    letter-spacing: -0.2px;
    white-space: nowrap;
  }
  .offer {
    position: absolute;
    left: 60px;
    top: 76px;
    font-size: 22px;
    font-weight: 700;
    line-height: 32px;
    white-space: nowrap;
  }
  .free-tag {
    position: absolute;
    left: 860px;
    top: 24px;
    font-size: 52px;
    font-weight: 700;
    line-height: 58px;
  }
  .disc {
    position: absolute;
    left: 985px;
    top: 26px;
  }
</style>
</head>
<body>
  <div class="banner">
    <div class="band" role="img" aria-label="Dark band with a subtle damask background"></div>

    <h1 class="headline">“How to Meditate Deeper than a Zen Monk!”</h1>

    <p class="offer">
      Request today and also receive daily to your inbox<br>
      "87 Easy Ways to Instantly Relax Your Mind and Body...FREE"
    </p>

    <div class="free-tag">Free<br>CD</div>

    <svg class="disc" width="118" height="118" viewBox="0 0 118 118" role="img" aria-label="Meditation CD showing a woman meditating in a calm blue setting">
      <defs>
        <radialGradient id="disc-fill" cx="50%" cy="45%" r="60%">
          <stop offset="0%" stop-color="var(--disc-light)"/>
          <stop offset="60%" stop-color="var(--disc-mid)"/>
          <stop offset="100%" stop-color="var(--disc-deep)"/>
        </radialGradient>
      </defs>
      <circle cx="59" cy="59" r="57" fill="url(#disc-fill)"/>
      <circle cx="59" cy="59" r="9" fill="var(--band-dark)"/>
    </svg>
  </div>
</body>
</html>
```